Seeking a new website design for electrical contracting company

Pelham & Tracy electrical contracting needs a new website for pelham-tracy.com

We are looking for modern and something real cool with motion for a landing page. we have some cool images from our photo shoot. maybe even 3d motion our existing logo. we would like something we can edit with news and events and update a past project page. Also allow to take payment
stock images at
https://mirabelwhitfordphotography.pixfolio-example.com/Pelham-and-Tracy

Target Market(s)

construction , home owners , business owners,

Industry/Entity Type

construction , electrical

Coding

Coded - Design and coding required

Number of Pages Required

5+ page

Font styles to use
Serif
Sans Serif

Colors
0054AA
0677BA
7BADD7
CADEEF
E8F1F8
0094D4
00A9DD
6FCCEA
C7EBF8
E9F6FB
FFF300
FFF600
FEFA6F
FFFEC7
FFFEE8

Requirements
Must have
• excitement, motion, selling professionalism,

```html
<!DOCTYPE html>
<html lang="en">
<head>
<meta charset="utf-8">
<title>Pelham &amp; Tracy – Electrical Contracting</title>
<link href="https://fonts.googleapis.com/css2?family=Montserrat:wght@500;700;800&family=Open+Sans:wght@400;600&display=swap" rel="stylesheet">
<style>
:root{
  --navy:#1e2766;
  --navy-deep:#151c4f;
  --orange:#f39200;
  --orange-soft:#f7b24a;
  --stage:#e6e7ec;
  --white:#ffffff;
  --cream:#f5f1ea;
  --ink:#2b2f45;
  --muted:#7a7f93;
  --photo-a:#8e9fb4;
  --photo-b:#c9b79a;
}
*{box-sizing:border-box;margin:0;padding:0}
html,body{width:732px;height:1200px;overflow:hidden;background:var(--stage)}
body{font-family:"Open Sans",Arial,sans-serif;color:var(--ink);display:flex;gap:24px;padding:20px 24px}
h1,h2,h3,.brand,.btn,.label{font-family:"Montserrat",Arial,sans-serif}
.page{width:330px;height:1160px;background:var(--white);display:flex;flex-direction:column;overflow:hidden;box-shadow:0 2px 8px rgba(0,0,0,.12)}
.photo{background:linear-gradient(135deg,var(--photo-a),var(--photo-b))}
.btn{display:inline-block;background:var(--orange);color:var(--white);font-size:5px;font-weight:700;padding:3px 8px;letter-spacing:.4px}
.title{font-size:12px;font-weight:800;text-align:center;color:var(--navy);letter-spacing:.5px}
.title span{color:var(--orange)}
.lead{font-size:4.5px;line-height:1.5;color:var(--muted);text-align:center;max-width:220px;margin:4px auto 0}

/* header */
.topbar{height:20px;background:var(--navy);display:flex;align-items:center;padding:0 8px 0 0;gap:6px}
.brand{background:var(--white);height:30px;align-self:flex-start;padding:0 6px;display:flex;align-items:center;gap:3px;font-size:6px;font-weight:800;color:var(--navy);position:relative;z-index:2}
.brand i{width:6px;height:6px;background:var(--orange);display:block}
.phone{font-size:4.5px;color:var(--white);display:flex;align-items:center;gap:2px;margin-left:auto}
.nav{display:flex;gap:5px;font-size:4px;color:var(--white);font-family:"Montserrat",sans-serif;font-weight:500}

/* hero */
.hero{height:190px;position:relative}
.hero-copy{position:absolute;left:18px;top:36px;color:var(--white)}
.hero h1{font-size:17px;line-height:1.1;font-weight:800;text-shadow:0 1px 2px rgba(0,0,0,.25)}
.hero h1 span{color:var(--orange)}
.hero p{font-size:4.5px;margin:5px 0 7px;max-width:130px;line-height:1.5}
.hero svg{position:absolute;left:0;bottom:0}

/* services */
.services{height:150px;padding:10px 18px 0}
.service-row{display:flex;justify-content:center;gap:10px;margin-top:10px}
.service{text-align:center;width:78px}
.hex{clip-path:polygon(25% 0,75% 0,100% 50%,75% 100%,25% 100%,0 50%);}
.service .hex{width:64px;height:56px;margin:0 auto}
.service .hex.bolt{background:var(--navy);display:flex;align-items:center;justify-content:center}
.card{width:78px;height:52px}
.label{font-size:4.5px;font-weight:700;color:var(--navy);margin-top:4px}

/* about */
.about{height:150px;background:var(--navy);position:relative;display:flex;align-items:center;gap:12px;padding:0 18px;overflow:hidden}
.about.light{background:var(--white)}
.about .stripe{position:absolute;width:120px;height:14px;background:var(--orange);transform:rotate(-20deg)}
.about .s1{left:-30px;top:6px}.about .s2{right:-30px;bottom:8px}
.about .collage{width:120px;height:100px;position:relative;z-index:1}
.about-copy{position:relative;z-index:1;flex:1}
.about h2{font-size:12px;font-weight:800;color:var(--white);margin-bottom:5px}
.about.light h2{color:var(--navy)}
.about h2 span{color:var(--orange)}
.about p{font-size:4.5px;line-height:1.5;color:#d9dcef;margin-bottom:6px}
.about.light p{color:var(--muted)}

/* projects */
.projects{height:150px;background:var(--cream);padding:12px 10px 0}
.project-row{display:flex;justify-content:center;gap:3px;margin-top:12px}
.project-row .hex{width:60px;height:66px;clip-path:polygon(50% 0,100% 25%,100% 75%,50% 100%,0 75%,0 25%)}
.project-row .tint{background:var(--orange)}
.project-row .hex:nth-child(even){margin-top:14px}

/* news */
.news{height:180px;padding:14px 18px 0}
.news-item{display:flex;gap:8px;margin-top:10px}
.news-item .photo{width:110px;height:58px;flex:none}
.news-item .date{display:inline-block;background:var(--orange);color:var(--white);font-size:4px;font-weight:700;padding:2px 4px;font-family:"Montserrat",sans-serif}
.news-item h3{font-size:6px;font-weight:700;color:var(--navy);margin:4px 0 3px;line-height:1.3}
.news-item p{font-size:4.5px;line-height:1.5;color:var(--muted)}

/* contact */
.contact{height:180px;display:flex;position:relative}
.contact .worker{width:140px;height:100%}
.contact-form{flex:1;padding:24px 14px 0}
.contact h2{font-size:12px;font-weight:800;color:var(--navy);margin-bottom:8px}
.contact h2 span{color:var(--orange)}
.field{display:block;font-size:4.5px;color:var(--muted);border-bottom:1px solid #cfd2dc;padding:6px 0 2px;margin-bottom:3px}
.field.tall{height:28px}
.contact .btn{margin-top:6px}

/* footer */
.footer{flex:1;background:var(--navy-deep);color:#c9cde6;padding:12px 16px;display:flex;gap:16px;border-top:3px solid var(--orange)}
.footer .brand{background:none;color:var(--white);height:auto;padding:0;align-self:flex-start}
.footer h3{font-size:5px;color:var(--white);font-weight:700;margin-bottom:4px}
.footer li{list-style:none;font-size:4.5px;line-height:1.8;display:flex;align-items:center;gap:3px}
.footer li b{width:3px;height:3px;background:var(--orange);display:inline-block}
.footer .copy{font-size:4px;margin-top:8px;color:#8f95bd}
</style>
</head>
<body>

<main class="page">
  <header class="topbar">
    <div class="brand"><i></i>Pelham &amp; Tracy</div>
    <div class="phone"><svg width="5" height="5" viewBox="0 0 10 10"><path d="M2 1l2 2-1 1.5a6 6 0 0 0 2.5 2.5L7 6l2 2-1.5 1.5C4 9 1 6 .5 2.5z" fill="#f39200"/></svg>(555) 014-2290</div>
    <nav class="nav"><span>HOME</span><span>ABOUT</span><span>SERVICES</span><span>PROJECTS</span><span>NEWS</span></nav>
    <span class="btn">GET A QUOTE</span>
  </header>

  <section class="hero photo" role="img" aria-label="Electrician in hard hat smiling in front of an electrical panel">
    <div class="hero-copy">
      <h1>POWERING<br><span>PRECISION</span> LIGHTING<br>THE FUTURE</h1>
      <p>Reliable electrical work for homes, businesses and builders across the region.</p>
      <span class="btn">LEARN MORE</span>
    </div>
    <svg width="330" height="26" viewBox="0 0 330 26"><path d="M0 14 L165 24 L330 6 L330 26 L0 26Z" fill="#fff"/><path d="M0 10 L165 20 L330 2 L330 6 L165 24 L0 14Z" fill="#f39200"/></svg>
  </section>

  <section class="services">
    <h2 class="title">OUR <span>SERVICES</span></h2>
    <p class="lead">Licensed electricians delivering safe, efficient and code compliant solutions for every project size.</p>
    <div class="service-row">
      <div class="service"><div class="hex photo" role="img" aria-label="Residential wiring work"></div><div class="label">RESIDENTIAL ELECTRICAL</div></div>
      <div class="service"><div class="hex bolt"><svg width="18" height="26" viewBox="0 0 18 26"><path d="M11 0 L1 15 H8 L6 26 L17 10 H10Z" fill="#f39200"/></svg></div><div class="label">COMMERCIAL ELECTRICAL</div></div>
      <div class="service"><div class="hex photo" role="img" aria-label="Industrial control panel work"></div><div class="label">INDUSTRIAL ELECTRICAL</div></div>
    </div>
  </section>

  <section class="about">
    <span class="stripe s1"></span><span class="stripe s2"></span>
    <div class="collage hex photo" role="img" aria-label="Collage of electricians at work"></div>
    <div class="about-copy">
      <h2>ABOUT <span>US</span></h2>
      <p>For over two decades our team has powered homes, offices and plants with careful planning, skilled crews and honest pricing on every job we take.</p>
      <span class="btn">READ MORE</span>
    </div>
  </section>

  <section class="projects">
    <h2 class="title">OUR <span>PROJECTS</span></h2>
    <div class="project-row">
      <div class="hex photo" role="img" aria-label="Project photo"></div>
      <div class="hex photo" role="img" aria-label="Project photo"></div>
      <div class="hex tint"></div>
      <div class="hex photo" role="img" aria-label="Project photo"></div>
      <div class="hex tint"></div>
    </div>
  </section>

  <section class="news">
    <h2 class="title">NEWS <span>&amp;</span> EVENTS</h2>
    <article class="news-item">
      <div class="photo" role="img" aria-label="Crew on a job site"></div>
      <div><span class="date">MAY 12, 2024</span><h3>New Solar Division Launches This Spring</h3><p>Our crews now install and service panel systems.</p></div>
    </article>
    <article class="news-item">
      <div class="photo" role="img" aria-label="Electrician inspecting wiring"></div>
      <div><span class="date">APR 28, 2024</span><h3>Safety Training Week For All Field Staff</h3><p>Every technician completed updated safety courses.</p></div>
    </article>
  </section>

  <section class="contact">
    <div class="worker photo" role="img" aria-label="Electrician in safety vest working at a panel"></div>
    <form class="contact-form">
      <h2>GET IN <span>TOUCH</span></h2>
      <span class="field">Full Name</span>
      <span class="field">Email Address</span>
      <span class="field">Phone</span>
      <span class="field tall">Message</span>
      <span class="btn">SUBMIT NOW</span>
    </form>
  </section>

  <footer class="footer">
    <div><div class="brand"><i></i>Pelham &amp; Tracy</div><p class="copy">© 2024 Pelham &amp; Tracy. All rights reserved.</p></div>
    <div><h3>SERVICES</h3><ul><li><b></b>Residential</li><li><b></b>Commercial</li><li><b></b>Industrial</li><li><b></b>Maintenance</li></ul></div>
    <div><h3>CONTACT US</h3><ul><li><b></b>(555) 014-2290</li><li><b></b>hello@pelham-tracy.com</li><li><b></b>pelham-tracy.com</li></ul></div>
  </footer>
</main>

<main class="page">
  <header class="topbar">
    <div class="brand"><i></i>Pelham &amp; Tracy</div>
    <div class="phone"><svg width="5" height="5" viewBox="0 0 10 10"><path d="M2 1l2 2-1 1.5a6 6 0 0 0 2.5 2.5L7 6l2 2-1.5 1.5C4 9 1 6 .5 2.5z" fill="#f39200"/></svg>(555) 014-2290</div>
    <nav class="nav"><span>HOME</span><span>ABOUT</span><span>SERVICES</span><span>PROJECTS</span><span>NEWS</span></nav>
    <span class="btn">GET A QUOTE</span>
  </header>

  <section class="hero photo" role="img" aria-label="Electrician in hard hat smiling in front of an electrical panel">
    <div class="hero-copy">
      <h1>POWERING<br><span>PRECISION</span> LIGHTING<br>THE FUTURE</h1>
      <p>Reliable electrical work for homes, businesses and builders across the region.</p>
      <span class="btn">LEARN MORE</span>
    </div>
    <svg width="330" height="26" viewBox="0 0 330 26"><path d="M0 14 L165 24 L330 6 L330 26 L0 26Z" fill="#fff"/><path d="M0 10 L165 20 L330 2 L330 6 L165 24 L0 14Z" fill="#f39200"/></svg>
  </section>

  <section class="services">
    <h2 class="title">OUR <span>SERVICES</span></h2>
    <p class="lead">Licensed electricians delivering safe, efficient and code compliant solutions for every project size.</p>
    <div class="service-row">
      <div class="service"><div class="card photo" role="img" aria-label="Residential wiring work"></div><div class="label">RESIDENTIAL ELECTRICAL</div></div>
      <div class="service"><div class="card photo" role="img" aria-label="Commercial lighting installation"></div><div class="label">COMMERCIAL ELECTRICAL</div></div>
      <div class="service"><div class="card photo" role="img" aria-label="Industrial control panel work"></div><div class="label">INDUSTRIAL ELECTRICAL</div></div>
    </div>
  </section>

  <section class="about light">
    <span class="stripe s1"></span><span class="stripe s2"></span>
    <div class="collage hex photo" role="img" aria-label="Collage of electricians at work"></div>
    <div class="about-copy">
      <h2>ABOUT <span>US</span></h2>
      <p>For over two decades our team has powered homes, offices and plants with careful planning, skilled crews and honest pricing on every job we take.</p>
      <span class="btn">READ MORE</span>
    </div>
  </section>

  <section class="projects">
    <h2 class="title">OUR <span>PROJECTS</span></h2>
    <div class="project-row">
      <div class="hex photo" role="img" aria-label="Project photo"></div>
      <div class="hex tint"></div>
      <div class="hex photo" role="img" aria-label="Project photo"></div>
      <div class="hex photo" role="img" aria-label="Project photo"></div>
      <div class="hex tint"></div>
    </div>
  </section>

  <section class="news">
    <h2 class="title">NEWS <span>&amp;</span> EVENTS</h2>
    <article class="news-item">
      <div class="photo" role="img" aria-label="Crew on a job site"></div>
      <div><span class="date">MAY 12, 2024</span><h3>New Solar Division Launches This Spring</h3><p>Our crews now install and service panel systems.</p></div>
    </article>
    <article class="news-item">
      <div class="photo" role="img" aria-label="Electrician inspecting wiring"></div>
      <div><span class="date">APR 28, 2024</span><h3>Safety Training Week For All Field Staff</h3><p>Every technician completed updated safety courses.</p></div>
    </article>
  </section>

  <section class="contact">
    <div class="worker photo" role="img" aria-label="Electrician in safety vest working at a panel"></div>
    <form class="contact-form">
      <h2>GET IN <span>TOUCH</span></h2>
      <span class="field">Full Name</span>
      <span class="field">Email Address</span>
      <span class="field">Phone</span>
      <span class="field tall">Message</span>
      <span class="btn">SUBMIT NOW</span>
    </form>
  </section>

  <footer class="footer">
    <div><div class="brand"><i></i>Pelham &amp; Tracy</div><p class="copy">© 2024 Pelham &amp; Tracy. All rights reserved.</p></div>
    <div><h3>SERVICES</h3><ul><li><b></b>Residential</li><li><b></b>Commercial</li><li><b></b>Industrial</li><li><b></b>Maintenance</li></ul></div>
    <div><h3>CONTACT US</h3><ul><li><b></b>(555) 014-2290</li><li><b></b>hello@pelham-tracy.com</li><li><b></b>pelham-tracy.com</li></ul></div>
  </footer>
</main>

</body>
</html>
```